Building company with a modern and unique product looking for a business card to help us stand out

We currently have a logo but as our business has grown, we feel that our business card is not reflecting our modern and high quality product and help us stand out from the crowd. Our business is mainly in the construction of new homes using a unique method and materials that makes our homes fire proof, vermin and pest resistant and rated to the maximum cyclone category (category 5). We need a business card that helps us stand out as well as communicating professionalism, high quality and trustworthiness. I have attached our current logo with a black and white option, as well as our business card which is double sided. We would like to retain as much of the information that is currently on our business cards, but presented in a more sleek way. We do like our current colour palette ( white, black, yellow and grey) and have been looking primarily at business cards with a black background however we are open to other combinations of colour and layout as long as we stand out. Please feel free to tweak our logo to make it more suitable for a business card, we like the black option that we use but we have had trouble trying to get the white area to match the rest of the logo and blend effectively into a business card. Please do not hesitate to contact us with any questions as we really want this to be successful!

Target Market(s)

Large contracts including government and larger companies

Industry/Entity Type

Business

We will be providing this business card to potential clients including key government ministers and large funding companies, our business card should show that we are professional and reliable.

Requirements
Must have
• It must be easy to read and pleasing to the eye, It must contain as much of the information on the current business card and unless something really stands out, we will most likely pick a design that has all of the information included. It must include our logo of course and have some colour included.
Nice to have
• We are looking for a high end business card and would like to see designs that reflect this. We like the gloss/matte contrast, plastic cards with opaque/coloured areas and unique features not seen on everyday paper business cards. It would be nice to see a few different colour combinations, we are open to new ideas so please feel free to take some artistic licence.
Should not have
• Must not be too busy, difficult to read or be distracting from the information conveyed. Other than this please feel free to add your own touches and make it unique!

```html
<!DOCTYPE html>
<html lang="en">
<head>
<meta charset="utf-8">
<title>Corbel Homes Co — Business Card</title>
<link rel="stylesheet" href="https://fonts.googleapis.com/css2?family=Montserrat:wght@600;700&family=Questrial&display=swap">
<style>
  :root {
    --page: #cdcdcd;
    --card: #2a2829;
    --gold: #c9a227;
    --gold-deep: #b8921c;
    --white: #ffffff;
    --grey: #8a8a8a;
    --rule: #3d3a3b;
    --ink: #2a2829;
  }
  * { box-sizing: border-box; margin: 0; padding: 0; }
  html, body { width: 1200px; height: 941px; overflow: hidden; }
  body {
    background: var(--page);
    font-family: "Questrial", sans-serif;
    position: relative;
  }
  .card {
    position: absolute;
    width: 540px;
    height: 330px;
    background: var(--card);
    overflow: hidden;
    box-shadow: 0 10px 24px rgba(0,0,0,0.25);
  }
  .card--front { left: 50px; top: 150px; }
  .card--back { left: 610px; top: 150px; }

  /* front */
  .front-stripe {
    position: absolute; left: 0; right: 0; bottom: 0;
    height: 30px; background: var(--gold);
  }
  .front-stripe::before {
    content: ""; position: absolute; left: 0; right: 0; top: -9px;
    height: 3px; background: var(--gold);
  }
  .brand {
    position: absolute; left: 34px; top: 138px;
    display: flex; align-items: center; gap: 9px;
    white-space: nowrap;
  }
  .brand-mark { width: 14px; height: 14px; background: var(--gold); flex: none; }
  .brand-name {
    font-family: "Questrial", sans-serif;
    font-size: 22px; color: var(--white); letter-spacing: 0.4px;
  }
  .divider {
    position: absolute; left: 282px; top: 60px;
    width: 1px; height: 180px; background: var(--rule);
  }
  .contact { position: absolute; left: 308px; top: 78px; }
  .contact-name {
    font-family: "Montserrat", sans-serif; font-weight: 700;
    color: var(--gold); font-size: 17px; letter-spacing: 0.5px;
  }
  .contact-role { color: var(--white); font-size: 13px; margin-top: 2px; }
  .contact-list { list-style: none; margin-top: 22px; }
  .contact-list li {
    display: flex; align-items: center; gap: 10px;
    color: var(--white); font-size: 13px; margin-bottom: 7px;
  }
  .icon {
    width: 16px; height: 16px; background: var(--gold); border-radius: 2px;
    display: flex; align-items: center; justify-content: center;
  }
  .icon svg { width: 11px; height: 11px; }

  /* back */
  .specialty { position: absolute; left: 34px; top: 34px; }
  .specialty-title {
    font-family: "Montserrat", sans-serif; font-weight: 700;
    color: var(--gold); font-size: 12.5px; line-height: 1.3; letter-spacing: 0.4px;
  }
  .specialty-list { list-style: none; margin-top: 8px; }
  .specialty-list li { color: var(--white); font-size: 13px; line-height: 1.45; }
  .specialty-list li::before { content: "· "; }
  .back-brand {
    position: absolute; right: 34px; top: 138px;
    display: flex; align-items: center; gap: 9px;
    white-space: nowrap;
  }
  .roof-art {
    position: absolute; left: 0; bottom: 0;
    width: 360px; height: 150px;
    background: linear-gradient(135deg, var(--gold) 0%, var(--gold-deep) 100%);
  }

  /* standalone wordmark */
  .wordmark {
    position: absolute; left: 830px; top: 700px;
    display: flex; align-items: center; gap: 12px;
    white-space: nowrap;
  }
  .wordmark .brand-mark { width: 20px; height: 20px; background: var(--ink); }
  .wordmark .brand-name { color: var(--ink); font-size: 32px; }
</style>
</head>
<body>

  <section class="card card--front">
    <div class="brand">
      <span class="brand-mark"></span>
      <span class="brand-name">Corbel Homes Co</span>
    </div>
    <div class="divider"></div>
    <div class="contact">
      <p class="contact-name">DANIEL WHITFORD</p>
      <p class="contact-role">Managing Director</p>
      <ul class="contact-list">
        <li><span class="icon"><svg viewBox="0 0 12 12"><rect x="3.5" y="1" width="5" height="10" rx="1" fill="none" stroke="#2a2829" stroke-width="1.3"/></svg></span>0400 555 018</li>
        <li><span class="icon"><svg viewBox="0 0 12 12"><path d="M2 1.5h2.5l1 2.5-1.5 1a6 6 0 0 0 3 3l1-1.5 2.5 1V11C5.5 11 1 6.5 2 1.5z" fill="#2a2829"/></svg></span>(02) 5550 1842</li>
        <li><span class="icon"><svg viewBox="0 0 12 12"><rect x="1" y="2.5" width="10" height="7" fill="none" stroke="#2a2829" stroke-width="1.2"/><path d="M1 2.5l5 4 5-4" fill="none" stroke="#2a2829" stroke-width="1.2"/></svg></span>hello@corbelhomes.com</li>
      </ul>
    </div>
    <div class="front-stripe"></div>
  </section>

  <section class="card card--back">
    <div class="specialty">
      <p class="specialty-title">SPECIALISING IN<br>HOMES THAT ARE</p>
      <ul class="specialty-list">
        <li>Fire Proof</li>
        <li>Climate Proof</li>
        <li>Cyclone Rated (Cat. 5)</li>
      </ul>
    </div>
    <div class="back-brand">
      <span class="brand-mark"></span>
      <span class="brand-name">Corbel Homes Co</span>
    </div>
    <div class="roof-art" role="img" aria-label="Large gold roofline graphic with white rooftop outlines and windows"></div>
  </section>

  <div class="wordmark">
    <span class="brand-mark"></span>
    <span class="brand-name">Corbel Homes Co</span>
  </div>

</body>
</html>
```